Web Design Project

The client is unsure if they want a completely new design or a design that matches their existing site closely (https://www.kelvatcover.com.au). So essentially we are looking for some designs that reflect the existing sites shape and colour and some designs that have their own new style. The company will sell three main types of insurance, Car, Bike and Caravan.

Read the complete brief and in the attached document.
The logo is also attached

I have also attached a zip of a few classic cars, if you can incorporate those.

Industry/Entity Type

Insurance

Requirements
Should not have
• Print This Page
Site Search

```html
<!DOCTYPE html>
<html lang="en">
<head>
<meta charset="utf-8">
<title>Kelvat Cover – Classic and Prestige Car and Bike Insurance</title>
<link rel="stylesheet" href="https://fonts.googleapis.com/css2?family=PT+Sans:ital,wght@0,400;0,700;1,700&family=Arimo:wght@400;700&family=Caveat:wght@500&display=swap">
<style>
:root{
  --ink:#222;
  --grey:#555;
  --mid:#777;
  --red:#c4161c;
  --red-dark:#a8141a;
  --orange:#f0a400;
  --orange-deep:#e79a00;
  --orange-light:#ffc93a;
  --menu:#f4b83a;
  --dark:#333;
  --footer:#4b4b4b;
  --line:#d6d6d6;
}
*{margin:0;padding:0;box-sizing:border-box}
html,body{width:1200px;height:995px;overflow:hidden;background:#fff}
body{position:relative;font-family:"PT Sans",sans-serif;color:var(--ink)}
.abs{position:absolute}
.topline{left:0;top:0;width:1200px;height:4px;background:var(--dark)}
.brand{left:110px;top:18px;width:206px;height:72px;display:flex;align-items:center;gap:10px}
.brand-dot{width:26px;height:26px;border-radius:50%;background:#1c1c1c}
.brand-name{font-family:"PT Sans",sans-serif;font-weight:700;font-size:24px;color:#1c1c1c;letter-spacing:1px}
.acct{top:4px;height:27px;background:#3b3b3b;border-radius:0 0 6px 6px;color:#fff;font:700 10px "Arimo",sans-serif;display:flex;align-items:center;justify-content:center;gap:6px}
.acct svg{width:11px;height:11px}
.callbox{left:831px;top:47px;width:52px;height:52px;border-radius:6px;background:linear-gradient(#e8424a,#b0141b)}
.callbox svg{width:52px;height:52px}
.insure{left:892px;top:46px;font-size:16px;color:var(--mid);font-weight:700}
.phone{left:892px;top:66px;font-size:15px;color:var(--red)}
.tag{left:893px;top:85px;font-size:11px;color:var(--red)}
.nav{left:0;top:108px;width:1200px;height:32px;background:linear-gradient(#ffd052,var(--orange))}
.nav a{position:absolute;top:8px;font:700 12px "Arimo",sans-serif;color:var(--ink);text-decoration:none;transform:translateX(-50%)}
.nav .current{position:absolute;left:231px;top:0;width:117px;height:32px;background:linear-gradient(#fff8e0,#f7c24b)}
.hero{left:0;top:140px;width:1200px;height:328px;background:radial-gradient(ellipse 420px 260px at 760px 170px,var(--orange-light),var(--orange) 70%,var(--orange-deep))}
.dropdown{left:231px;top:135px;width:171px;height:76px;background:var(--menu);z-index:3}
.dropdown a{display:block;height:38px;line-height:40px;padding-left:22px;color:#fff;font-size:12px;text-decoration:none}
.dropdown a+a{border-top:1px solid #f8cf72;line-height:28px}
.vehicle{left:115px;top:185px;width:505px;height:245px;border-radius:40px 60px 20px 20px;background:linear-gradient(#2a2a2a,#0c0c0c)}
.benefits-title{left:650px;top:176px;font:italic 700 27px "PT Sans",sans-serif;color:#fff;text-shadow:1px 2px 2px rgba(0,0,0,.45);letter-spacing:-.5px}
.benefits{font-size:12px;color:var(--ink);list-style:none}
.benefits li{height:23px;display:flex;align-items:center;gap:7px}
.benefits li::before{content:"";width:12px;height:12px;border-radius:50%;background:radial-gradient(circle at 40% 40%,#ffb27a,#d2451b)}
.thumb{top:391px;width:85px;height:54px;border-radius:6px;border:1px solid #555}
.arrow-btn{width:15px;height:15px;border-radius:50%;background:#e7a000;border:1px solid #333}
.arrow-btn svg{width:13px;height:13px;display:block}
.band{left:0;top:468px;width:1200px;height:42px;background:#f1a500;border-top:1px solid #ffcf5a}
.band-text{left:126px;top:471px;font:500 25px "Caveat",cursive;color:#fff}
.band-ctrl{left:1052px;top:484px;width:36px;height:12px}
.events{left:0;top:510px;width:1200px;height:112px;background:#fff;box-shadow:0 8px 10px -4px rgba(0,0,0,.18)}
.events-title{left:110px;top:530px;width:202px;text-align:right;font:italic 700 25px "PT Sans",sans-serif;color:var(--red);letter-spacing:-.8px}
.events-intro{left:110px;top:565px;width:201px;text-align:right;font:11px/18px "Arimo",sans-serif;color:var(--grey)}
.vdiv{width:1px;background:var(--line)}
.event-name{font-size:13px;color:var(--red)}
.event-pic{width:57px;height:46px;border:2px solid #fff;box-shadow:0 0 2px rgba(0,0,0,.4)}
.event-text{font-size:11px;line-height:16px;color:var(--grey);width:150px}
.cta{left:110px;width:227px;height:42px;background:linear-gradient(#3a3a3a,#050505);color:#fff;font:italic 700 18px "PT Sans",sans-serif;padding:10px 0 0 20px;letter-spacing:-.8px}
.cta i{position:absolute;right:14px;top:6px;width:32px;height:30px;border-radius:50%;background:#999}
.cta i.ring{background:radial-gradient(circle,#000 35%,#f07a20 36% 70%,transparent 71%)}
.main-title{left:362px;top:646px;font-size:20px;color:var(--red)}
.main-copy{left:367px;top:684px;width:720px;font-size:11px;line-height:18px;color:var(--grey)}
.sub-title{font:italic 700 18px "PT Sans",sans-serif;color:var(--red-dark);letter-spacing:-.4px}
.partners{left:110px;top:792px;width:501px;height:96px;border:1px solid #ccc}
.badge{top:814px;height:48px;background:#d9d9d9}
.side-arrow{top:825px;width:24px;height:30px;border-radius:5px;background:linear-gradient(#eee,#999)}
.quote{font:700 30px Georgia,serif;color:#bbb}
.news-pic{left:654px;top:807px;width:103px;height:72px;border:3px solid #fff;box-shadow:0 0 3px rgba(0,0,0,.4);background:linear-gradient(#eef0f2,#b8bcc2)}
.news-copy{left:772px;top:807px;width:310px;font-size:11px;line-height:18px;color:var(--mid)}
.news-copy a{color:var(--red);text-decoration:none}
.footer{left:0;top:920px;width:1200px;height:75px;background:var(--footer)}
.foot-nav{left:110px;top:941px;font:11px "Arimo",sans-serif;color:#fff;display:flex;gap:0}
.foot-nav span{white-space:pre}
.copyright{left:110px;top:962px;font:11px "Arimo",sans-serif;color:#fff}
.follow{left:936px;top:949px;font:11px "Arimo",sans-serif;color:#fff}
.social{top:941px;width:27px;height:27px;border-radius:4px;background:linear-gradient(#7fa2d2,#3c6299)}
</style>
</head>
<body>
<div class="abs topline"></div>

<header>
  <div class="abs brand"><span class="brand-dot"></span><span class="brand-name">KELVAT COVER</span></div>
  <div class="abs acct" style="left:871px;width:107px">BROKER LOGIN <svg viewBox="0 0 12 12"><circle cx="6" cy="6" r="6" fill="#fff"/><path d="M3 5l3 3 3-3" stroke="#333" stroke-width="1.6" fill="none"/></svg></div>
  <div class="abs acct" style="left:981px;width:107px">REGISTER <svg viewBox="0 0 12 12"><circle cx="6" cy="6" r="6" fill="#fff"/><path d="M3 5l3 3 3-3" stroke="#333" stroke-width="1.6" fill="none"/></svg></div>
  <div class="abs callbox"><svg viewBox="0 0 52 52"><path d="M17 13c2-1 4 0 5 2l3 5c1 2 0 3-1 4l-2 1c1 4 5 8 9 9l1-2c1-1 2-2 4-1l5 3c2 1 3 3 2 5l-2 3c-2 2-6 2-11-1-5-3-11-9-14-14-3-5-3-9-1-11z" fill="#fff"/></svg></div>
  <div class="abs insure">INSURE WITH AN ENTHUSIAST</div>
  <div class="abs phone">1300 555 014</div>
  <div class="abs tag">Classic and Prestige Car and Bike Insurance</div>
</header>

<nav class="abs nav">
  <span class="current"></span>
  <a style="left:167px">Home</a>
  <a style="left:289px">About Us</a>
  <a style="left:424px">Insurance</a>
  <a style="left:552px">Events</a>
  <a style="left:669px">Clubs</a>
  <a style="left:781px">Links</a>
  <a style="left:889px">FAQ</a>
  <a style="left:1013px">Contact Us</a>
</nav>

<section class="abs hero"></section>
<div class="abs dropdown"><a>Terms and Conditions</a><a>Careers</a></div>
<div class="abs vehicle" role="img" aria-label="Black luxury SUV, three-quarter front view"></div>
<h2 class="abs benefits-title">Our Policy Benefits</h2>
<ul class="abs benefits" style="left:647px;top:224px">
  <li>Agreed Value</li><li>New Replacement Vehicle in first 2 years</li><li>Choice of Repairer</li><li>Lifetime Guarantee for Repairs</li><li>Free Windscreen/Glass Benefit</li>
</ul>
<ul class="abs benefits" style="left:886px;top:224px">
  <li>Hire car following accident or theft</li><li>Flexible coverage</li><li>Pay Premiums by Instalments</li><li>Salvage retained by you on</li><li>vehicles over 30 years</li>
</ul>
<div class="abs arrow-btn" style="left:676px;top:411px"><svg viewBox="0 0 13 13"><path d="M8 3L4.5 6.5 8 10" stroke="#222" stroke-width="1.6" fill="none"/></svg></div>
<div class="abs thumb" style="left:697px;background:linear-gradient(#444,#111)" role="img" aria-label="Car dashboard stereo"></div>
<div class="abs thumb" style="left:791px;background:linear-gradient(#ddd,#666)" role="img" aria-label="Black sports motorbike"></div>
<div class="abs thumb" style="left:884px;background:linear-gradient(#777,#222)" role="img" aria-label="Dark car front detail"></div>
<div class="abs thumb" style="left:978px;background:linear-gradient(#a9c3e2,#6f8f4f)" role="img" aria-label="Caravan parked on grass"></div>
<div class="abs arrow-btn" style="left:1067px;top:411px"><svg viewBox="0 0 13 13"><path d="M5 3l3.5 3.5L5 10" stroke="#222" stroke-width="1.6" fill="none"/></svg></div>

<div class="abs band"></div>
<div class="abs band-text">The Specialised car insurance cover your Classic or Prestige car needs</div>
<svg class="abs band-ctrl" viewBox="0 0 36 12"><path d="M1 2l5 4-5 4z" fill="#fff"/><rect x="11" y="2" width="3" height="8" fill="#fff"/><rect x="16" y="2" width="3" height="8" fill="#fff"/><path d="M24 2l5 4-5 4zM30 2l5 4-5 4z" fill="#fff"/></svg>

<section class="abs events"></section>
<h2 class="abs events-title">Upcoming Events</h2>
<p class="abs events-intro">Lorem Ipsum is simply dummy text of the printing and typesetting industry.</p>
<div class="abs vdiv" style="left:344px;top:526px;height:80px;box-shadow:1px 0 2px #ccc"></div>
<div class="abs vdiv" style="left:598px;top:536px;height:68px"></div>
<div class="abs vdiv" style="left:846px;top:536px;height:68px"></div>

<div class="abs event-name" style="left:370px;top:535px">Ashvale Classic Show'n'Shine</div>
<div class="abs event-pic" style="left:370px;top:558px;background:linear-gradient(#f4f4f4,#bbb)" role="img" aria-label="White coupe"></div>
<p class="abs event-text" style="left:440px;top:562px">A fabulous day out for the family to come and view some.</p>

<div class="abs event-name" style="left:618px;top:535px">2012 Sydney Jamboree</div>
<div class="abs event-pic" style="left:618px;top:558px;background:linear-gradient(#c8ccd8,#2a3060)" role="img" aria-label="Blue motorbike"></div>
<p class="abs event-text" style="left:688px;top:562px">A fabulous day out for the family to come and view some.</p>

<div class="abs event-name" style="left:868px;top:535px">4th Brookfield Valley Street Meet</div>
<div class="abs event-pic" style="left:868px;top:558px;background:linear-gradient(#b9c7d0,#555)" role="img" aria-label="Silver sedan"></div>
<p class="abs event-text" style="left:938px;top:562px">A fabulous day out for the family to come and view some.</p>

<div class="abs cta" style="top:649px">REQUEST A QUOTE<i></i></div>
<div class="abs cta" style="top:699px">VEHICLES WE INSURE<i class="ring"></i></div>

<h1 class="abs main-title" style="font-weight:400">The Specialised car insurance cover your Classic or Prestige car needs</h1>
<p class="abs main-copy">Kelvat Cover shares your passion for classic cars, vintage cars, prestige cars and hot rods.&nbsp; Don't just trust your specialist vehicle insurance to a general insurance provider – we're specialists, we've only insured cars like yours and will cover your car like it's one of our own. Call today to find out how much more we can do for you.</p>

<h3 class="abs sub-title" style="left:116px;top:760px">Affiliations</h3>
<div class="abs partners"></div>
<div class="abs side-arrow" style="left:105px"></div>
<div class="abs badge" style="left:136px;width:128px"></div>
<div class="abs badge" style="left:279px;width:83px;border-radius:8px"></div>
<div class="abs badge" style="left:378px;top:830px;height:35px;width:120px"></div>
<div class="abs badge" style="left:508px;width:75px"></div>
<div class="abs side-arrow" style="left:594px"></div>

<h3 class="abs sub-title" style="left:637px;top:760px">News on all things Motoring</h3>
<div class="abs quote" style="left:637px;top:784px">“</div>
<div class="abs news-pic" role="img" aria-label="Black luxury sedan"></div>
<p class="abs news-copy">In almost 50 years, the expectations were high on the latest offering from the Varenne sportscar. It has taken almost 50 years, Varenne has pushed themselves to satisfy even the harshest of critics to offer what is being hailed as "the best V7 yet" &nbsp;<a>Read more...</a></p>
<div class="abs quote" style="left:1076px;top:860px">”</div>

<footer class="abs footer"></footer>
<div class="abs foot-nav"><span>Home          |          About Us          |          Insurance          |          Events          |          Clubs          |          Links          |          FAQ          |          Contact Us</span></div>
<div class="abs copyright">Copyright © 2013 Kelvat Cover. All Rights Reserved.</div>
<div class="abs follow">Follow Us :</div>
<div class="abs social" style="left:998px"></div>
<div class="abs social" style="left:1028px;background:linear-gradient(#9fdcf0,#3aa3c9)"></div>
<div class="abs social" style="left:1058px"></div>
</body>
</html>
```